DuePoint.com website design

We are a collection agency that collects debt from past residents of apartments on behalf of Property Management Companies. We are want to design a 3 page website with - Home - How it Works - Schedule Demo. We'd like a sketch of a skyline showing high rise apartment buildings, houses, shops, etc. We would like for there to be some animation, possibly clouds and the sun slowly moving. Maybe kids playing ball or catch or something like that. Bird flying and landing. An electric car charging (to indicate we are modern). We are looking for a friendly community vibe. The site will also need a button "Property Managers Login". When some comes to the site we would like a pop up that says "Property Managers Click Here/Past Residents Click Here" with a different icon for each that relates to the description. I've included a link to a test site we had designed so feel free to use some of the copy from it. We just aren't happy with the design. On the Home page our tag line should be "Get more payments, faster, from past residents!" and "Digital First, NOT Digital Only". All without transaction fees, we don't get paid unless we get you paid first!
Additional selling points:

24 hour virtual agent and virtual telephone agent so we don't miss any opportunities to GET YOUR MONEY!

Old school collection strategies meet cutting edge technology to create effective work flow algorithms to put the best debt collectors on your accounts with data driven intelligence to determine the best way to get paid.

No Subscription Fees
No Payment Processing Fees
No Software Fees
No Mail, Email or TXT Fees

Inquire about our FIRST PARTY accounts receivable outsourcing. You may qualify for free post move out A/R processing and AI payment negotiator for the low hanging fruit. Don't pay full collection commission when there wasn't a full collection attempt!

For the How it Works page - See the page from our previous design. I will include the link below. Please come up with your own version of this but you can use the copy from this page.

The schedule demo page will be a form that will feed to our CRM that will include:
Name
Email
Company
Title
Phone Number
Number of Units
Tell us how we can help you: (a box for them provide details)

Also include our phone number at the bottom with something like

Here is a link to our previous design test site:
https://brelmora-preview.example/duepoint-new/
I've attached an image of the back end so you can get an idea of the colors we need, I've also included our logo. For the most part we would like most of the site to match the blue colors from our logo, but we do need to incorporate some of the yellow in the images I've attached. Possibly make the buttons on the site the yellow color? Make the sun Match the yellow? I'll leave it up to you.

```html
<!DOCTYPE html>
<html lang="en">
<head>
<meta charset="utf-8">
<title>DuePoint – Schedule Demo</title>
<link href="https://fonts.googleapis.com/css2?family=Lato:wght@300;400;700&display=swap" rel="stylesheet">
<style>
:root{
  --navy:#0f3e6e;
  --ink:#1c2233;
  --muted:#7a879e;
  --placeholder:#9aa5b6;
  --line:#e3e6ea;
  --footer-bg:#1b1b1b;
  --footer-text:#c9c9c9;
  --accent:#fbbf6f;
  --teal:#21a9c4;
}
*{box-sizing:border-box;margin:0;padding:0}
html,body{width:1031px;height:1200px;overflow:hidden;background:#fff;font-family:'Lato',sans-serif;color:var(--ink)}
.page{position:relative;width:1031px;height:1200px}
.abs{position:absolute}

.brand{left:75px;top:22px;display:flex;align-items:center;gap:7px;font-size:22px;font-weight:700;color:var(--navy)}
.brand-mark{width:22px;height:22px;border:3px solid var(--teal);border-radius:5px}
.nav a{position:absolute;top:29px;font-size:11px;color:var(--muted);text-decoration:none}
.btn{position:absolute;display:flex;align-items:center;justify-content:center;font-size:11px;text-decoration:none}
.btn-login{left:713px;top:19px;width:72px;height:34px;border:1px solid var(--navy);color:var(--navy)}
.btn-pm{left:794px;top:19px;width:165px;height:34px;background:var(--navy);color:#fff}

.title{left:72px;top:142px;font-size:40px;font-weight:700;letter-spacing:-0.5px}
.lede{left:72px;top:202px;width:360px;font-size:11px;line-height:17px;color:var(--muted)}
.divider{left:72px;top:306px;width:429px;height:1px;background:var(--line)}
.find-title{left:72px;top:378px;font-size:16px;font-weight:400}
.card{position:absolute;width:178px;height:57px;border:1px solid var(--line);display:flex;align-items:center;padding-left:18px;gap:19px;font-size:11px}
.card svg{width:20px;height:20px;flex:none}

.field{position:absolute;left:573px;width:386px;height:50px;border:1px solid var(--line);padding:0 17px;display:flex;align-items:center;font-size:11px;color:var(--placeholder)}
.field.filled{color:var(--ink)}
.field.active{border-color:var(--ink)}
.field .label{position:absolute;left:17px;top:-6px;background:#fff;padding:0 6px;font-size:8px;color:var(--ink)}
.field.area{align-items:flex-start;padding-top:19px}
.btn-send{left:573px;top:747px;width:172px;height:43px;background:var(--navy);color:#fff;font-size:13px}

.footer{left:0;top:862px;width:1031px;height:338px;background:var(--footer-bg)}
.foot-brand{left:77px;top:944px;display:flex;align-items:center;gap:10px;font-size:38px;font-weight:700;color:#fff}
.foot-brand-mark{width:44px;height:44px;border:5px solid #fff;border-radius:12px}
.pitch{left:475px;top:935px;width:480px;font-size:17px;line-height:23px;color:var(--footer-text);font-weight:400}
.pitch-sub{left:475px;top:997px;font-size:16px;color:#fff;font-weight:700}
.foot-nav a{position:absolute;top:1075px;font-size:11px;color:#fff;text-decoration:none}
.btn-contact{left:475px;top:1065px;width:98px;height:35px;background:var(--accent);color:var(--ink)}
.social{position:absolute;top:1065px;width:35px;height:35px;border:1px solid #fff;display:flex;align-items:center;justify-content:center}
.social span{width:12px;height:12px;border:1.5px solid #fff;border-radius:50%}
.foot-rule{left:72px;top:1134px;width:887px;height:1px;background:#4a4a4a}
.copyright{left:0;top:1154px;width:1031px;text-align:center;font-size:12px;color:#a9a9a9}
.copyright b{color:#fff;font-weight:400}
.copyright i{font-style:normal;margin:0 7px}
</style>
</head>
<body>
<div class="page">
  <header>
    <div class="abs brand"><span class="brand-mark"></span>DuePoint</div>
    <nav class="nav">
      <a style="left:417px" href="#">Home</a>
      <a style="left:475px" href="#">How It Works</a>
      <a style="left:571px" href="#">About US</a>
      <a style="left:647px" href="#">Contact</a>
    </nav>
    <a class="btn btn-login" href="#">Login</a>
    <a class="btn btn-pm" href="#">Property Managers Login</a>
  </header>

  <main>
    <h1 class="abs title">Schedule Demo</h1>
    <p class="abs lede">Lorem ipsum dolor sit amet, consectetur adipiscing elit. Sollicitudin nunc eget amet, quam risus nisi, justo.</p>
    <div class="abs divider"></div>
    <h2 class="abs find-title">Where to Find us</h2>

    <div class="card" style="left:72px;top:416px">
      <svg viewBox="0 0 24 24"><path fill="#1c2233" d="M6.6 10.8a15 15 0 0 0 6.6 6.6l2.2-2.2c.3-.3.7-.4 1-.2 1.1.4 2.3.6 3.6.6.6 0 1 .4 1 1V20c0 .6-.4 1-1 1A17 17 0 0 1 3 4c0-.6.4-1 1-1h3.5c.6 0 1 .4 1 1 0 1.3.2 2.5.6 3.6.1.3 0 .7-.2 1z"/></svg>Phone Number</div>
    <div class="card" style="left:268px;top:416px">
      <svg viewBox="0 0 24 24"><rect x="2" y="4" width="20" height="16" rx="4" fill="#1c2233"/><path d="M7 10l5 3 5-3" stroke="#fff" stroke-width="1.6" fill="none"/></svg>Email</div>
    <div class="card" style="left:72px;top:490px"><svg viewBox="0 0 24 24"><circle cx="12" cy="12" r="8" fill="#1c2233"/></svg>Circlefeed</div>
    <div class="card" style="left:268px;top:490px"><svg viewBox="0 0 24 24"><circle cx="12" cy="12" r="8" fill="#1c2233"/></svg>Chirpline</div>
    <div class="card" style="left:72px;top:565px"><svg viewBox="0 0 24 24"><rect x="4" y="4" width="16" height="16" fill="#1c2233"/></svg>Workbridge</div>
    <div class="card" style="left:268px;top:565px"><svg viewBox="0 0 24 24"><rect x="4" y="4" width="16" height="16" fill="#1c2233"/></svg>Snapframe</div>

    <form>
      <div class="field filled" style="top:164px"><span class="label">Name</span>Marlo Fenwick</div>
      <div class="field filled active" style="top:233px"><span class="label">Email Address</span>marlofenwick123@mail |</div>
      <div class="field" style="top:301px">Company</div>
      <div class="field" style="top:370px">Title</div>
      <div class="field" style="top:439px">Phone Number</div>
      <div class="field" style="top:508px">Number of Units</div>
      <div class="field area" style="top:576px;height:142px">Tell us how we can help you</div>
      <a class="btn btn-send" href="#">Send Schedule Demo</a>
    </form>
  </main>

  <footer>
    <div class="abs footer"></div>
    <div class="abs foot-brand"><span class="foot-brand-mark"></span>DuePoint</div>
    <p class="abs pitch">LET DUEPOINT EARN YOUR BUSINESS, IF WE DON'T GET YOU PAID WE DON'T CHARGE YOU ANYTHING</p>
    <p class="abs pitch-sub">We Want To Earn Your Business</p>
    <nav class="foot-nav">
      <a style="left:72px" href="#">Home</a>
      <a style="left:147px" href="#">How It Works</a>
      <a style="left:260px" href="#">Schedule Demo</a>
      <a style="left:382px" href="#">About US</a>
    </nav>
    <a class="btn btn-contact" href="#">Contact Us</a>
    <a class="social" style="left:788px" href="#"><span></span></a>
    <a class="social" style="left:833px" href="#"><span></span></a>
    <a class="social" style="left:879px" href="#"><span></span></a>
    <a class="social" style="left:925px" href="#"><span></span></a>
    <div class="abs foot-rule"></div>
    <p class="abs copyright">©2022 All rights reserved by <b>DuePoint</b><i>•</i>Privacy Policy<i>•</i>Term Conditions</p>
  </footer>
</div>
</body>
</html>
```